Need Letterhead Design & Matching Business Card

I have a logo that I love already. But the letterhead is less than appealing and boring. I'd like a design for my letterhead which I will match with business cards. Also, I'd like to have used fonts that are generally available, as my current letterhead uses a font named "SPACE" which nobody has unless they download it...so when a Word version is forwarded, it looks awful on the receiver's screed due to not having the font. That being said, modern is the look we like and are going for.

My business is "Halloran Brightmoor PC" - a law firm specializing in representing people who have suffered catastrophic injuries or death (plane, auto, train crashes etc.).

See attached letterhead, which has all of the pertinent information. My logo is also attached in various formats.

```html
<!DOCTYPE html>
<html lang="en">
<head>
<meta charset="utf-8">
<title>Halloran Brightmoor PC – Stationery</title>
<link rel="stylesheet" href="https://fonts.googleapis.com/css2?family=Arimo:wght@400;700&family=Barlow+Condensed:wght@400;600&display=swap">
<style>
  :root{
    --navy:#1a4f85;
    --slate:#37444d;
    --ink:#2d2a2b;
    --text:#3f4549;
    --muted:#5b6166;
    --paper:#ffffff;
    --paper-back:#eceef0;
    --stage:#f3f4f5;
    --edge:#e6e8ea;
  }
  *{margin:0;padding:0;box-sizing:border-box}
  html,body{width:1200px;height:918px;overflow:hidden;background:var(--stage)}
  body{font-family:"Arimo",Arial,sans-serif;color:var(--text)}
  .canvas{position:relative;width:1200px;height:918px}

  /* Envelopes */
  .envelope{position:absolute;left:94px;width:489px;height:231px}
  .envelope--navy{top:127px}
  .envelope--slate{top:494px}
  .envelope__back{position:absolute;left:0;top:0;width:381px;height:201px;background:var(--paper-back)}
  .envelope__flap{position:absolute;left:0;top:0;width:381px;height:65px;border-radius:0 0 0 48px}
  .envelope--navy .envelope__flap{background:var(--navy)}
  .envelope--slate .envelope__flap{background:var(--slate)}
  .envelope__front{position:absolute;left:107px;top:30px;width:382px;height:201px;
    background:linear-gradient(#fff 60%,#f1f2f4);overflow:hidden}
  .envelope__swoosh{position:absolute;left:0;top:0;width:382px;height:60px}
  .envelope__addr{position:absolute;font-size:7px;line-height:10px;text-align:center;color:var(--text)}

  .brand{position:absolute;font-family:"Arimo",Arial,sans-serif;font-weight:700;color:var(--slate);
    text-transform:uppercase;letter-spacing:.02em;line-height:1.05}
  .brand-square{position:absolute;background:var(--slate)}

  /* Letterhead */
  .letterhead{position:absolute;left:660px;top:94px;width:481px;height:725px;background:var(--paper);
    border:3px solid var(--edge);overflow:hidden}
  .letterhead__swoosh{position:absolute;left:0;top:0;width:481px;height:60px}
  .letterhead .brand{left:216px;top:59px;font-size:17px;color:var(--ink)}
  .letterhead .brand-square{left:376px;top:49px;width:63px;height:63px;background:var(--ink)}
  .sender{position:absolute;left:22px;top:96px;font-size:11px;font-weight:700;color:var(--slate)}
  .sender-addr{position:absolute;left:22px;top:114px;font-size:11px;color:var(--muted)}
  .salutation{position:absolute;left:30px;top:181px;font-size:19px;font-weight:700;color:#111}
  .recipient-role{position:absolute;left:93px;top:205px;font-size:12px;color:#111}
  .closing{position:absolute;left:42px;top:574px;font-size:15px;color:#111}
  .signature{position:absolute;left:42px;top:596px;width:120px;height:66px;
    background:linear-gradient(90deg,#f6f6f6,#ececec)}
  .signer{position:absolute;left:46px;top:669px;font-size:15px;color:#111}
  .contact{position:absolute;left:312px;top:633px;list-style:none;
    font-family:"Barlow Condensed",Arial Narrow,sans-serif;font-size:11px;color:var(--muted)}
  .contact li{display:flex;align-items:center;height:21.5px}
  .contact li.web{font-weight:600;color:#222}
  .contact svg{width:14px;height:14px;margin-right:8px;flex:none}
</style>
</head>
<body>
<div class="canvas">

  <!-- Envelope, navy variant -->
  <section class="envelope envelope--navy" aria-label="Envelope, navy variant">
    <div class="envelope__back"><div class="envelope__flap"></div></div>
    <div class="envelope__front">
      <svg class="envelope__swoosh" viewBox="0 0 382 60" preserveAspectRatio="none">
        <path d="M0 46 C90 12 200 0 280 0 H382 V40 C300 4 120 6 0 46 Z" fill="var(--navy)"/>
        <path d="M0 46 C120 6 300 4 382 40 V57 C280 12 110 14 0 46 Z" fill="var(--slate)"/>
      </svg>
      <div class="brand-square" style="left:26px;top:90px;width:40px;height:40px"></div>
      <div class="brand" style="left:76px;top:96px;font-size:11px">Halloran<br>Brightmoor PC</div>
      <p class="envelope__addr" style="left:47px;top:147px;width:100px">4820 Larkspur Ave.<br>Suite 600<br>Westbrook, CA 90415</p>
    </div>
  </section>

  <!-- Envelope, slate variant -->
  <section class="envelope envelope--slate" aria-label="Envelope, slate variant">
    <div class="envelope__back"><div class="envelope__flap"></div></div>
    <div class="envelope__front">
      <svg class="envelope__swoosh" viewBox="0 0 382 60" preserveAspectRatio="none">
        <path d="M0 46 C90 12 200 0 280 0 H382 V40 C300 4 120 6 0 46 Z" fill="var(--slate)"/>
        <path d="M0 46 C120 6 300 4 382 40 V57 C280 12 110 14 0 46 Z" fill="var(--navy)"/>
      </svg>
      <div class="brand" style="left:24px;top:97px;font-size:11px">Halloran<br>Brightmoor PC</div>
      <div class="brand-square" style="left:122px;top:97px;width:85px;height:85px"></div>
      <p class="envelope__addr" style="left:17px;top:150px;width:100px">4820 Larkspur Ave.<br>Suite 600<br>Westbrook, CA 90415</p>
    </div>
  </section>

  <!-- Letterhead -->
  <article class="letterhead" aria-label="Letterhead">
    <svg class="letterhead__swoosh" viewBox="0 0 481 60" preserveAspectRatio="none">
      <path d="M0 0 H400 C450 10 470 35 481 47 C380 0 150 5 0 35 Z" fill="var(--slate)"/>
      <path d="M0 35 C150 5 380 0 481 47 C380 15 150 15 0 57 Z" fill="var(--navy)"/>
    </svg>
    <div class="brand">Halloran<br>Brightmoor PC</div>
    <div class="brand-square"></div>
    <p class="sender">R. Dalton Mercer, Esq. | President</p>
    <p class="sender-addr">4820 Larkspur Ave. | suite 600 &nbsp;I&nbsp;&nbsp; Westbrook, CA 90415</p>

    <h1 class="salutation">Dear Jhon Smith</h1>
    <p class="recipient-role">Manager Director</p>

    <p class="closing">Best Regads</p>
    <div class="signature" role="img" aria-label="Handwritten signature"></div>
    <p class="signer">Halloran</p>

    <ul class="contact">
      <li><svg viewBox="0 0 14 14"><circle cx="7" cy="7" r="7" fill="#111"/><rect x="5" y="3.5" width="4" height="7" rx=".8" fill="none" stroke="#fff" stroke-width="1"/></svg>Tel: (555) 014-2290</li>
      <li><svg viewBox="0 0 14 14"><circle cx="7" cy="7" r="7" fill="#111"/><rect x="4" y="5" width="6" height="4.2" fill="#fff"/><path d="M4 5 L7 7.4 L10 5" fill="none" stroke="#111" stroke-width=".7"/></svg>dalton@halloranbrightmoor.com</li>
      <li class="web"><svg viewBox="0 0 14 14"><circle cx="7" cy="7" r="7" fill="#111"/><circle cx="7" cy="7" r="3.2" fill="none" stroke="#fff" stroke-width=".8"/><path d="M3.8 7 H10.2 M7 3.8 V10.2" stroke="#fff" stroke-width=".7"/></svg>www.halloranbrightmoor.com</li>
    </ul>
  </article>

</div>
</body>
</html>
```